Envoys Trophy - Mexico (Cricket)

This year The Halvern Bat League is hosting a tournament called the Envoys Trophy, on March 22nd at our Club (Quintal Sporting Club) in Mexico City

4 teams lead by the respective Ambassadors (GB, Australia, India and Mexico) will compete for a Cup in the twenty/20 format of the game of cricket

We want as many people to come as possible hence need a flyer to put on the websites of the various embassies plus other societies like The Corlan Fellowship, PELORAN society (Southern Pacific Friends Circle Group etc)

We are also looking at sponsors who are interested in being involved with cricket due to its potential in Mexico, its brand value, as well as its links in countries such as India – for example the biggest cinema group here (Vistarama) is opening cinemas in India and would like to be involved. Brevik Motorworks is now an Indian company etc.

So if you could come up with something that looks professional, and attracts the interest of sponsors and spectators that would be great – the event will also attract the interest of the media, and will be followed by our Garden Gala, which is also something for which we will need a flyer.

The tournament's first game is at 11.am
Refreshments will be available
Sponsors will also be showcasing their products
Kids welcome
Address - Quintal Sporting Club, Santa Clara de Mizquitlan, Cerro Pinto, Mexico

Target Market(s)

The flyer aims to attract the interest of spectators (families) from the various communities involved (British, Australian, Indian and Mexican) for a high end event that we will look to repeat every year.
We also want to attract the interest of sponsors of high end brands who want to be associated with the event.

Industry/Entity Type

Club

Requirements
Must have
• Logo of Halvern Bat League

```html
<!DOCTYPE html>
<html lang="en">
<head>
<meta charset="utf-8">
<title>Envoys Trophy – Halvern Bat League</title>
<link rel="stylesheet" href="https://fonts.googleapis.com/css2?family=Macondo&family=Oswald:wght@400;500&display=swap">
<style>
  :root {
    --ink-black: #0b0405;
    --wine-deep: #3a0d14;
    --wine: #6b1f2c;
    --wine-light: #8a3a48;
    --cream: #efeedb;
    --cream-shadow: #2a1a12;
    --white: #ffffff;
    --olive: #8a8f2e;
    --badge: #f4f4f4;
  }
  * { box-sizing: border-box; margin: 0; padding: 0; }
  html, body { width: 1200px; height: 1000px; overflow: hidden; background: var(--ink-black); }
  .flyer {
    position: relative; width: 1200px; height: 1000px; overflow: hidden;
    background:
      radial-gradient(ellipse 520px 560px at 520px 470px, rgba(11,4,5,0.95) 0%, rgba(11,4,5,0) 100%),
      linear-gradient(160deg, var(--wine-deep) 0%, var(--ink-black) 40%, var(--wine) 85%, var(--wine-light) 100%);
    font-family: "Oswald", "Arial Narrow", sans-serif;
    color: var(--white);
  }
  .ball-art { position: absolute; left: 360px; top: 350px; width: 1200px; height: 400px; }
  .ball-art svg { display: block; }

  .club-mark { position: absolute; left: 12px; top: 40px; width: 190px; display: flex; flex-direction: column; align-items: center; gap: 10px; }
  .club-mark .dot { width: 110px; height: 110px; border-radius: 50%; background: var(--olive); }
  .club-mark .name { font-family: "Oswald", sans-serif; font-weight: 400; font-size: 22px; color: var(--cream); text-align: center; line-height: 1.1; }

  .presenter { position: absolute; top: 50px; left: 0; width: 1200px; text-align: center; font-size: 20px; letter-spacing: -0.5px; }
  .presenter .big { font-size: 32px; }

  .title { position: absolute; left: 0; width: 1200px; text-align: center; font-family: "Macondo", "Papyrus", cursive; color: var(--cream);
    text-shadow: 3px 3px 0 var(--cream-shadow), -1px -1px 0 var(--cream-shadow), 5px 6px 10px rgba(0,0,0,0.7); line-height: 1; }
  .title-top { top: 160px; font-size: 165px; letter-spacing: 6px; }
  .title-bottom { top: 315px; font-size: 165px; letter-spacing: 6px; }

  .coming-soon { position: absolute; left: 935px; top: 115px; font-size: 46px; transform: rotate(52deg); transform-origin: left top; white-space: nowrap; }
  .teaser { position: absolute; left: 118px; top: 420px; font-size: 25px; line-height: 1.05; text-align: center; transform: rotate(22deg); width: 250px; }
  .review { position: absolute; left: 735px; top: 565px; transform: rotate(-7deg); font-weight: 500; }
  .review .quote { font-size: 26px; display: block; }
  .review .source { font-size: 18px; display: block; text-align: right; padding-right: 70px; }

  .details { position: absolute; left: 0; top: 752px; width: 1200px; text-align: center; line-height: 1.02; letter-spacing: -0.5px; }
  .details p { white-space: nowrap; }
  .details small { font-size: 20px; }
  .details b { font-weight: 400; font-size: 36px; }
  .date { position: absolute; left: 0; top: 918px; width: 1200px; text-align: center; font-size: 52px; line-height: 1; }

  .badge-rating { position: absolute; left: 10px; top: 912px; width: 335px; height: 72px; background: var(--badge); border: 3px solid var(--ink-black); }
  .badge-format { position: absolute; left: 1012px; top: 915px; width: 165px; height: 75px; background: var(--badge); border-radius: 4px; }
</style>
</head>
<body>
<main class="flyer">
  <div class="ball-art" role="img" aria-label="Glowing cricket ball wrapped in drifting red smoke">
    <svg width="840" height="400" viewBox="0 0 840 400">
      <defs>
        <radialGradient id="ballGlow" cx="0.42" cy="0.4" r="0.65">
          <stop offset="0" stop-color="#ffffff"/>
          <stop offset="0.35" stop-color="#d9b8be"/>
          <stop offset="0.8" stop-color="#7a3a46"/>
          <stop offset="1" stop-color="#3a0d14"/>
        </radialGradient>
        <radialGradient id="smokeHaze" cx="0.5" cy="0.5" r="0.5">
          <stop offset="0" stop-color="#a05060" stop-opacity="0.45"/>
          <stop offset="1" stop-color="#a05060" stop-opacity="0"/>
        </radialGradient>
      </defs>
      <ellipse cx="560" cy="120" rx="300" ry="220" fill="url(#smokeHaze)"/>
      <circle cx="200" cy="195" r="182" fill="url(#ballGlow)"/>
    </svg>
  </div>

  <div class="club-mark">
    <span class="dot"></span>
    <span class="name">Halvern Bat League</span>
  </div>

  <p class="presenter">THE <span class="big">HALVERN BAT LEAGUE</span> PRESENTS</p>

  <h1 class="title title-top">ENVOYS</h1>
  <p class="title title-bottom">TROPHY</p>

  <p class="coming-soon">COMING SOON!</p>
  <p class="teaser">WATCH THE STORY UNFOLD AS FOUR TEAMS COMPETE FOR THE ULTIMATE PRIZE</p>
  <p class="review"><span class="quote">"THRILLING FROM START TO FINISH"</span><span class="source">-PITCHSIDE DIGEST</span></p>

  <section class="details">
    <p><small>JOIN US FOR A </small><b>CRICKET TOURNAMENT</b><small> FIRST GAME STARTS AT 11AM</small></p>
    <p><small>LOCATED AT </small><b>QUINTAL SPORTING CLUB, SANTA CLARA DE MIZQUITLAN, CERRO PINTO, MEXICO</b></p>
    <p><b>REFRESHMENTS AVAILABLE</b><small> SPONSORS WILL BE SHOWCASING </small><b>PRODUCTS</b><small> KIDS ARE WELCOME</small></p>
  </section>

  <p class="date">MARCH 22ND</p>

  <div class="badge-rating" role="img" aria-label="Audience rating badge"></div>
  <div class="badge-format" role="img" aria-label="Format badge"></div>
</main>
</body>
</html>
```